Cedarmoor business card for handing simple contact information and generating service awareness

Utilizing the attached logo(s), generate a professional, but approachable, card conveying a sense of capability and integrity. Please only use one logo of the four attached; the different colors are all acceptable, but preference will be given to a design integrating a teal/turquoise logo,

I do not know where to put in the contact information or details?

Target Market(s)

Agriculture, Farming, Timber, Forestry, Construction, Crane Service

Industry/Entity Type

Contact Information for Business Card

Name, Phone Number, email address

Colors

Designer to choose colors to be used in the design.

Requirements
Nice to have
• It would be great to have either a mountain or one of the attached cranes as a backdrop on the rear of the card. Simple watermarks and/or Debossing is also great

```html
<!DOCTYPE html>
<html lang="en">
<head>
<meta charset="utf-8">
<title>Cedarmoor – Business Card</title>
<link rel="stylesheet" href="https://fonts.googleapis.com/css2?family=Montserrat:wght@400;500;800&display=swap">
<style>
  :root {
    --stage: #c4c4c4;
    --card-dark: #1e1e1e;
    --teal: #2a7a6a;
    --ink-light: #f2f2f2;
    --forest-deep: #141a16;
    --forest-mid: #24331f;
    --forest-light: #3b4a2a;
  }
  * { box-sizing: border-box; margin: 0; padding: 0; }
  html, body { width: 1200px; height: 815px; overflow: hidden; }
  body {
    background: var(--stage);
    font-family: "Montserrat", sans-serif;
    position: relative;
  }
  .card {
    position: absolute;
    width: 540px;
    height: 309px;
    border-radius: 2px;
    box-shadow: 0 10px 24px rgba(0,0,0,.28);
    overflow: hidden;
  }
  /* Front */
  .card-front { left: 40px; top: 150px; background: var(--card-dark); }
  .front-brand {
    position: absolute; right: 44px; top: 40px;
    display: flex; align-items: center; gap: 10px;
  }
  .brand-dot {
    width: 20px; height: 20px; border-radius: 50%; background: var(--teal);
  }
  .brand-name {
    font-weight: 500; font-size: 28px; letter-spacing: .5px;
    color: var(--teal);
  }
  .divider {
    position: absolute; left: 34px; right: 22px; top: 148px;
    height: 2px; background: var(--teal);
  }
  .accent-block {
    position: absolute; left: 0; top: 92px; width: 16px; height: 48px; background: var(--teal);
  }
  .person { position: absolute; left: 34px; top: 88px; }
  .person-name {
    font-weight: 800; font-size: 28px; letter-spacing: 1.5px;
    text-transform: uppercase; color: var(--teal); line-height: 1.1;
  }
  .person-role {
    font-weight: 500; font-size: 14px; letter-spacing: .5px;
    text-transform: uppercase; color: var(--ink-light); margin-top: 2px;
  }
  .contacts { position: absolute; left: 34px; top: 166px; list-style: none; }
  .contacts li {
    display: flex; align-items: center; gap: 9px;
    font-size: 14.5px; color: var(--ink-light); height: 26px;
  }
  .contacts svg { width: 13px; height: 13px; fill: var(--teal); flex: none; }
  .address {
    position: absolute; right: 26px; top: 170px; text-align: right;
    font-size: 14.5px; line-height: 1.45; color: var(--ink-light); font-style: normal;
  }
  /* Back */
  .card-back {
    left: 620px; top: 356px;
    display: flex; align-items: center; justify-content: center;
  }
  .backdrop {
    position: absolute; inset: 0;
    background:
      radial-gradient(ellipse at 70% 20%, var(--forest-light) 0%, transparent 55%),
      linear-gradient(180deg, var(--forest-mid) 0%, var(--forest-deep) 55%, #1b241c 75%, #0f1411 100%);
  }
  .back-brand {
    position: relative; display: flex; align-items: center; gap: 12px;
  }
  .back-brand .brand-dot { width: 28px; height: 28px; }
  .back-brand .brand-name { font-size: 40px; }
</style>
</head>
<body>
  <section class="card card-front" aria-label="Business card front">
    <div class="front-brand">
      <span class="brand-dot"></span>
      <span class="brand-name">Cedarmoor</span>
    </div>
    <div class="accent-block"></div>
    <div class="person">
      <h1 class="person-name">Dana Hollis</h1>
      <p class="person-role">Manager</p>
    </div>
    <div class="divider"></div>
    <ul class="contacts">
      <li><svg viewBox="0 0 24 24"><path d="M6.6 10.8a15 15 0 0 0 6.6 6.6l2.2-2.2a1 1 0 0 1 1-.25 11.4 11.4 0 0 0 3.6.57 1 1 0 0 1 1 1V20a1 1 0 0 1-1 1A17 17 0 0 1 3 4a1 1 0 0 1 1-1h3.5a1 1 0 0 1 1 1c0 1.25.2 2.45.57 3.57a1 1 0 0 1-.25 1z"/></svg>(555)210-4417</li>
      <li><svg viewBox="0 0 24 24"><path d="M7 1h10a2 2 0 0 1 2 2v18a2 2 0 0 1-2 2H7a2 2 0 0 1-2-2V3a2 2 0 0 1 2-2zm0 3v14h10V4z"/></svg>(555)318-62045</li>
      <li><svg viewBox="0 0 24 24"><path d="M2 5h20v14H2zm2 2v.5l8 5 8-5V7l-8 5z"/></svg>hello@cedarmoor.com</li>
      <li><svg viewBox="0 0 24 24"><path d="M12 2a10 10 0 1 0 0 20 10 10 0 0 0 0-20zm-1 2.1V8H7.3A8 8 0 0 1 11 4.1zm2 0A8 8 0 0 1 16.7 8H13zM4.6 10H11v4H4.6a8 8 0 0 1 0-4zm8.4 0h6.4a8 8 0 0 1 0 4H13zm-5.7 6H11v3.9A8 8 0 0 1 7.3 16zm5.7 0h3.7A8 8 0 0 1 13 19.9z"/></svg>www.cedarmoor.com</li>
    </ul>
    <address class="address">42 Alder Ridge Lane<br>Pinecrest, ST 00000</address>
  </section>

  <section class="card card-back" aria-label="Business card back">
    <div class="backdrop" role="img" aria-label="Dark forest river scene with trees reflected in still water"></div>
    <div class="back-brand">
      <span class="brand-dot"></span>
      <span class="brand-name">Cedarmoor</span>
    </div>
  </section>
</body>
</html>
```